Athletic Director Business Card

I need a business card that is very appealing and shows my school logo and colours (red, white and black). We just finished changing our school logo and have sent the two logos we use and I have also sent the logo W that we also use. I'm not sure if combining them works but I thought I would send it anyway and let your creative juices flow. Looking for a simple but very luring design. It could have the different sports on it but I think doing something with the logo is probably the direction I would like to see as we offer 11 different sports and 22 different teams so that might get to busy. We have a long "Tradition of Excellence" and maybe that could be on the card. If you need to change to logo by shadowing it, or making it a two colour with a glow in it or what every you think would make it look fantastic give it a try as I'm open to different looks.

Target Market(s)

Parents of high school athletes, businesses throughout our city, principals.

Industry/Entity Type

School

Requirements
Must have
• Name of School - Ridgemont Valley High School or just Ridgemont Valley.
My Name - Marcus Holloway
Position - Athletic Director
Phone - 403-555-0147
Cell - 403-555-0183
Email - mkholloway@pvsd.ab.ca
Website - www.ridgemontvalleyathletics.com

```html
<!DOCTYPE html>
<html lang="en">
<head>
<meta charset="utf-8">
<title>Ridgemont Valley Athletics – Business Card</title>
<link rel="stylesheet" href="https://fonts.googleapis.com/css2?family=Tinos:ital,wght@0,400;0,700;1,400&display=swap">
<style>
  :root {
    --red: #b3161f;
    --red-deep: #8e1118;
    --black: #111111;
    --ink: #1d1d1d;
    --paper: #ffffff;
    --backdrop: #e9e6e1;
    --photo-light: #e9b7a8;
    --photo-mid: #c9303a;
    --photo-dark: #3a2a2a;
  }
  * { box-sizing: border-box; margin: 0; padding: 0; }
  html, body { width: 1200px; height: 858px; overflow: hidden; }
  body {
    background: var(--backdrop);
    font-family: "Tinos", "Times New Roman", serif;
    color: var(--ink);
    position: relative;
  }
  .card {
    position: absolute;
    width: 540px;
    height: 309px;
    background: var(--paper);
    box-shadow: 0 6px 20px rgba(0,0,0,0.18);
    overflow: hidden;
  }
  .card--front { left: 40px; top: 275px; }
  .card--back { left: 620px; top: 275px; }

  /* Front */
  .team-photo { position: absolute; left: 0; bottom: 0; width: 540px; height: 309px; }
  .brand-mark {
    position: absolute; top: 30px; right: 34px;
    display: flex; align-items: center; gap: 7px;
    color: var(--red); font-weight: 700; font-size: 15px; letter-spacing: 0.5px;
  }
  .brand-mark__square { width: 12px; height: 12px; background: var(--red); }
  .identity { position: absolute; left: 34px; top: 96px; }
  .identity__name { font-size: 19px; letter-spacing: 1.5px; text-transform: uppercase; font-weight: 400; }
  .identity__role { font-size: 13px; margin-top: 4px; padding-left: 12px; }
  .contact {
    position: absolute; right: 28px; top: 120px;
    list-style: none; text-align: right; font-size: 13px; line-height: 22px;
  }
  .contact li { display: flex; justify-content: flex-end; align-items: center; gap: 10px; }
  .contact svg { width: 10px; height: 10px; flex: none; }
  .contact li:last-child { margin-top: 34px; }

  /* Back */
  .school { position: absolute; left: 120px; top: 70px; }
  .school__name { font-size: 22px; font-weight: 400; }
  .school__rule { width: 150px; height: 1.5px; background: var(--black); margin: 12px 0 12px -20px; }
  .school__motto { font-size: 13px; font-style: italic; }
  .back-band { position: absolute; left: 0; bottom: 0; width: 540px; height: 309px; }
  .back-mark {
    position: absolute; right: 34px; bottom: 34px;
    color: var(--red); font-weight: 700; font-size: 16px; letter-spacing: 0.5px;
  }
</style>
</head>
<body>
  <section class="card card--front" aria-label="Business card front">
    <svg class="team-photo" viewBox="0 0 540 309" role="img" aria-label="Team photo of the volleyball squad in red and black uniforms">
      <defs>
        <linearGradient id="photoTone" x1="0" y1="0" x2="1" y2="1">
          <stop offset="0" stop-color="var(--photo-light)"/>
          <stop offset="0.5" stop-color="var(--photo-mid)"/>
          <stop offset="1" stop-color="var(--photo-dark)"/>
        </linearGradient>
      </defs>
      <path d="M0,165 Q240,150 340,309 L0,309 Z" fill="url(#photoTone)"/>
    </svg>
    <div class="brand-mark"><span class="brand-mark__square"></span>Ridgemont Valley</div>
    <div class="identity">
      <h1 class="identity__name">Marcus Holloway</h1>
      <p class="identity__role">Athletic Director</p>
    </div>
    <ul class="contact">
      <li>403-555-0147
        <svg viewBox="0 0 10 10"><path d="M2 1h2l1 2.5-1.2 1a5 5 0 0 0 2.7 2.7l1-1.2L10 7v2a1 1 0 0 1-1 1A9 9 0 0 1 0 1a1 1 0 0 1 1-1z" fill="var(--black)"/></svg></li>
      <li>403-555-0183
        <svg viewBox="0 0 10 10"><rect x="2.5" y="0.5" width="5" height="9" rx="1" fill="none" stroke="var(--black)"/></svg></li>
      <li>mkholloway@pvsd.ab.ca
        <svg viewBox="0 0 10 10"><rect x="0.5" y="2" width="9" height="6" fill="var(--black)"/><path d="M0.5 2l4.5 3.5L9.5 2" stroke="var(--paper)" fill="none"/></svg></li>
      <li>www.ridgemontvalleyathletics.com
        <svg viewBox="0 0 10 10"><circle cx="5" cy="5" r="4.5" fill="var(--black)"/></svg></li>
    </ul>
  </section>

  <section class="card card--back" aria-label="Business card back">
    <div class="school">
      <h2 class="school__name">Ridgemont Valley High School</h2>
      <div class="school__rule"></div>
      <p class="school__motto">“Tradition of Excellence”</p>
    </div>
    <svg class="back-band" viewBox="0 0 540 309" aria-hidden="true">
      <path d="M0,228 Q250,175 540,200 L540,309 L0,309 Z" fill="var(--black)"/>
      <path d="M0,228 Q250,175 540,200" fill="none" stroke="var(--red)" stroke-width="3"/>
    </svg>
    <div class="back-mark">Ridgemont Valley</div>
  </section>
</body>
</html>
```